Tovally's Pest Control Billboard

I need a billboard designed for my pest control company. Feel free to check out our website, www.tovallys-example.com. I can also provide any logo, etc for design help. It should be funny but show trust. We want to focus on Mice and rodents. Phone # 555-013-7291 should be used. Shouldn't be to scary, we never use fear to sell.

Target Market(s)

People with pest issues, Mice, Rodents

Industry/Entity Type

Pest Control

Font styles to use
Sans Serif

Colors
59FF00
82FF00
B8FF75
E3FFCB
F4FFEA

Requirements
Must have
• Humor
Nice to have
• Some humor

```html
<!DOCTYPE html>
<html lang="en">
<head>
<meta charset="utf-8">
<title>Tovally's Pest Control Billboard</title>
<link href="https://fonts.googleapis.com/css2?family=Oswald:wght@500;600&family=Montserrat:ital,wght@0,700;0,800;1,800&display=swap" rel="stylesheet">
<style>
  :root {
    --page-bg: #e9ecef;
    --board-bg: #ffffff;
    --brand-green: #4f9a1c;
    --ink: #111111;
    --tick: #4f9a1c;
    --art-tone-a: #f3d9c2;
    --art-tone-b: #c98a5e;
  }
  * { margin: 0; padding: 0; box-sizing: border-box; }
  html, body { width: 1200px; height: 1200px; overflow: hidden; }
  body {
    background: var(--page-bg);
    display: flex; align-items: center; justify-content: center;
    font-family: "Montserrat", sans-serif;
    color: var(--ink);
  }
  .billboard {
    position: relative;
    width: 1120px; height: 520px;
    background: var(--board-bg);
    box-shadow: 0 6px 24px rgba(0,0,0,.15);
    overflow: hidden;
  }
  .content {
    position: absolute; left: 30px; top: 30px; width: 760px;
  }
  .brand {
    display: flex; align-items: center; justify-content: center; gap: 12px;
    font-weight: 800; font-size: 32px; color: var(--brand-green);
    margin-bottom: 26px;
  }
  .brand-dot {
    width: 20px; height: 20px; border-radius: 50%; background: var(--brand-green);
  }
  .headline {
    font-family: "Oswald", sans-serif; font-weight: 600;
    font-size: 34px; line-height: 1.05; color: var(--brand-green);
    text-transform: uppercase; letter-spacing: -0.4px; white-space: nowrap;
  }
  .subhead {
    font-family: "Oswald", sans-serif; font-weight: 500;
    font-size: 26px; line-height: 1.1; text-transform: uppercase;
    margin: 8px 0 0 50px; letter-spacing: -0.3px; white-space: nowrap;
  }
  .rule { height: 2px; background: var(--ink); margin: 10px 60px 16px 30px; }
  .services {
    position: relative; height: 90px; list-style: none;
    font-weight: 700; font-size: 19px; text-transform: uppercase;
  }
  .services li { position: absolute; display: flex; align-items: center; gap: 6px; white-space: nowrap; }
  .services svg { width: 15px; height: 15px; }
  .s-bird { left: 0; top: 30px; }
  .s-mouse { left: 100px; top: 60px; }
  .s-bugs { left: 200px; top: 0; }
  .s-mosquito { left: 290px; top: 38px; }
  .s-bedbugs { left: 470px; top: 0; }
  .cta {
    font-weight: 800; font-style: italic; font-size: 20px;
    text-transform: uppercase; margin: 26px 0 0 50px; white-space: nowrap;
  }
  .contact-band {
    position: absolute; left: 0; bottom: 0;
    width: 840px; height: 82px;
    background: var(--brand-green);
    border-top-right-radius: 16px;
    display: flex; align-items: center; gap: 10px;
    padding-left: 30px;
    color: #fff; font-weight: 800; white-space: nowrap;
  }
  .contact-band svg { width: 28px; height: 28px; flex: none; }
  .contact-band .phone { font-size: 30px; }
  .contact-band .divider { font-size: 30px; font-weight: 700; }
  .contact-band .web { font-size: 25px; }
  .mascot-art {
    position: absolute; right: 30px; top: 24px;
    width: 250px; height: 380px;
    border-radius: 20px;
    background: radial-gradient(circle at 50% 55%, var(--art-tone-a), var(--art-tone-b));
  }
</style>
</head>
<body>
  <main class="billboard">
    <section class="content">
      <div class="brand"><span class="brand-dot"></span>Tovally's Pest Control</div>
      <h1 class="headline">Wisconsin Pest Control &amp; Extermination Services</h1>
      <p class="subhead">Servicing both residential and commercial customers</p>
      <div class="rule"></div>
      <ul class="services">
        <li class="s-bird"><svg viewBox="0 0 16 16"><circle cx="8" cy="8" r="6.5" fill="none" stroke="var(--tick)" stroke-width="1.6"/><path d="M4.8 8.2l2.2 2.2 4.2-4.6" fill="none" stroke="var(--tick)" stroke-width="1.8"/></svg>Bird control</li>
        <li class="s-mouse"><svg viewBox="0 0 16 16"><circle cx="8" cy="8" r="6.5" fill="none" stroke="var(--tick)" stroke-width="1.6"/><path d="M4.8 8.2l2.2 2.2 4.2-4.6" fill="none" stroke="var(--tick)" stroke-width="1.8"/></svg>Mouse control</li>
        <li class="s-bugs"><svg viewBox="0 0 16 16"><circle cx="8" cy="8" r="6.5" fill="none" stroke="var(--tick)" stroke-width="1.6"/><path d="M4.8 8.2l2.2 2.2 4.2-4.6" fill="none" stroke="var(--tick)" stroke-width="1.8"/></svg>Bugs &amp; insects</li>
        <li class="s-mosquito"><svg viewBox="0 0 16 16"><circle cx="8" cy="8" r="6.5" fill="none" stroke="var(--tick)" stroke-width="1.6"/><path d="M4.8 8.2l2.2 2.2 4.2-4.6" fill="none" stroke="var(--tick)" stroke-width="1.8"/></svg>Mosquito control</li>
        <li class="s-bedbugs"><svg viewBox="0 0 16 16"><circle cx="8" cy="8" r="6.5" fill="none" stroke="var(--tick)" stroke-width="1.6"/><path d="M4.8 8.2l2.2 2.2 4.2-4.6" fill="none" stroke="var(--tick)" stroke-width="1.8"/></svg>Bedbugs control</li>
      </ul>
      <p class="cta">Call today! To schedule your free home inspection</p>
    </section>

    <footer class="contact-band">
      <svg viewBox="0 0 24 24" aria-hidden="true"><path d="M6.6 2.5l3 3.2-1.8 2.4c.9 2.4 3 4.6 5.6 5.9l2.3-1.8 3.3 2.9-1.7 3.1c-6.8.3-13.6-6.6-13-13.4z" fill="#fff"/></svg>
      <span class="phone">(555) 013-7291</span>
      <span class="divider">|</span>
      <svg viewBox="0 0 24 24" aria-hidden="true"><g fill="none" stroke="#fff" stroke-width="1.6"><circle cx="12" cy="12" r="9.5"/><ellipse cx="12" cy="12" rx="4" ry="9.5"/><path d="M2.5 12h19M4 7h16M4 17h16"/></g></svg>
      <span class="web">www.tovallys-example.com</span>
    </footer>

    <div class="mascot-art" role="img" aria-label="Cartoon mouse waving a white flag of surrender inside a red no-entry circle"></div>
  </main>
</body>
</html>
```